Welding Fabrication and Inspection Business Card Design

Welding Fabrication and Inspection Services,

Business

Industrial Machinery ServicesMohammed Rahim30 Ballarat Street, Mount Gravatt East.4122.QLD

```html
<!DOCTYPE html>
<html lang="en">
<head>
<meta charset="utf-8">
<title>Tarnwell Forge Services – Business Card</title>
<link href="https://fonts.googleapis.com/css2?family=Roboto:wght@400;500;700&display=swap" rel="stylesheet">
<style>
  :root{
    --page:#e4e2de;
    --card-light:#f4f4f4;
    --card-silver:#cfcfcf;
    --band-dark:#2a2a2c;
    --band-edge:#4a4a4c;
    --ink-light:#ffffff;
    --ink-dark:#3a3a3c;
    --ink-muted:#8a8a8c;
    --photo-main:#8e2a2e;
    --photo-shade:#3b3b3b;
  }
  html,body{margin:0;padding:0;width:1200px;height:950px;overflow:hidden;background:var(--page);}
  body{font-family:"Roboto",Arial,sans-serif;}
  .sheet{width:1200px;height:950px;display:flex;flex-direction:column;align-items:center;justify-content:center;gap:30px;}
  .card{position:relative;width:760px;height:434px;overflow:hidden;
    background:linear-gradient(135deg,var(--card-light) 0%,#ffffff 45%,var(--card-silver) 100%);
    box-shadow:0 6px 18px rgba(0,0,0,.18);}
  .card-art{position:absolute;inset:0;width:100%;height:100%;}

  /* back */
  .product-photo{position:absolute;left:260px;top:70px;width:240px;height:180px;border-radius:6px;
    background:radial-gradient(ellipse at 50% 35%,var(--photo-main) 0%,#6e2226 45%,var(--photo-shade) 100%);}
  .back-web{position:absolute;right:48px;bottom:54px;font-size:21px;letter-spacing:4px;color:var(--ink-muted);font-weight:400;}

  /* front */
  .identity{position:absolute;left:54px;top:48px;color:var(--ink-light);}
  .identity .name{font-size:32px;font-weight:700;margin:0;letter-spacing:.5px;}
  .identity .role{font-size:19px;font-weight:400;margin:2px 0 0;}
  .contact{position:absolute;left:54px;top:150px;color:var(--ink-light);font-size:20px;line-height:29px;list-style:none;margin:0;padding:0;}
  .contact li{display:flex;align-items:center;gap:10px;}
  .contact .address{margin-bottom:4px;}
  .contact svg{width:17px;height:17px;fill:var(--ink-light);flex:none;}
  .brand{position:absolute;right:40px;bottom:64px;display:flex;align-items:center;gap:12px;}
  .brand-name{font-size:26px;font-weight:700;color:var(--ink-dark);}
  .brand-dot{width:14px;height:14px;border-radius:50%;background:var(--ink-muted);}
</style>
</head>
<body>
<main class="sheet">

  <section class="card card-back" aria-label="Card back">
    <div class="product-photo" role="img" aria-label="Photo of a red magnetic particle inspection yoke with hinged legs"></div>
    <p class="back-web">TarnwellForgeServices.com</p>
  </section>

  <section class="card card-front" aria-label="Card front">
    <svg class="card-art" viewBox="0 0 760 434" aria-hidden="true">
      <polygon points="0,0 520,0 575,92 165,434 0,434" fill="var(--band-dark)"/>
      <line x1="150" y1="434" x2="575" y2="92" stroke="#ffffff" stroke-width="4"/>
      <line x1="130" y1="434" x2="560" y2="88" stroke="var(--band-edge)" stroke-width="2"/>
      <circle cx="580" cy="88" r="10" fill="#ffffff" stroke="#bdbdbd" stroke-width="2"/>
    </svg>

    <div class="identity">
      <h1 class="name">Khalid Nasser</h1>
      <p class="role">President</p>
    </div>

    <ul class="contact">
      <li class="address">17 Corrowen Street<br>Brackenvale East. 4190.QLD</li>
      <li><svg viewBox="0 0 24 24"><path d="M6.6 10.8a15 15 0 0 0 6.6 6.6l2.2-2.2a1 1 0 0 1 1-.25 11.4 11.4 0 0 0 3.6.57 1 1 0 0 1 1 1V20a1 1 0 0 1-1 1A17 17 0 0 1 3 4a1 1 0 0 1 1-1h3.5a1 1 0 0 1 1 1c0 1.25.2 2.45.57 3.57a1 1 0 0 1-.25 1z"/></svg>786 555 0142</li>
      <li><svg viewBox="0 0 24 24"><path d="M2 5h20v14H2z M3.5 6.5 12 13l8.5-6.5" fill="none" stroke="#fff" stroke-width="2"/></svg>khalid@tarnwellforge.com</li>
      <li><svg viewBox="0 0 24 24"><circle cx="12" cy="12" r="10"/><circle cx="12" cy="12" r="4" fill="var(--band-dark)"/></svg>www.tarnwellforge.com</li>
    </ul>

    <div class="brand">
      <span class="brand-dot"></span>
      <span class="brand-name">Tarnwell Forge Services</span>
    </div>
  </section>

</main>
</body>
</html>
```